Business Card For Kelmora Financial Consulting

Hi, I would like a business card designed. Bold, modern.
Please use the same design as the logo. I have also attached the website design to see the overall theme.
Wordmark Font
Color: Hex: #01AEF7

```html
<!DOCTYPE html>
<html lang="en">
<head>
<meta charset="utf-8">
<title>Kelmora Financial Consulting – Business Card</title>
<link href="https://fonts.googleapis.com/css2?family=Montserrat:wght@400;500;700&display=swap" rel="stylesheet">
<style>
  :root {
    --page: #ffffff;
    --navy: #1c2f3a;
    --blue: #2194d1;
    --bright: #01aef7;
    --white: #ffffff;
  }
  * { margin: 0; padding: 0; box-sizing: border-box; }
  html, body { width: 809px; height: 1200px; overflow: hidden; background: var(--page); }
  body { position: relative; font-family: "Montserrat", sans-serif; }

  .card {
    position: absolute;
    left: 84px;
    width: 640px;
    height: 366px;
    overflow: hidden;
  }
  .card-front { top: 194px; background: var(--navy); }
  .card-back { top: 640px; background: var(--blue); }
  .card-shape { position: absolute; inset: 0; width: 100%; height: 100%; }

  .brand {
    position: absolute;
    left: 304px;
    top: 168px;
    display: flex;
    align-items: center;
    gap: 10px;
  }
  .brand-mark {
    width: 40px;
    height: 40px;
    border: 3px solid var(--bright);
  }
  .brand-text { display: flex; flex-direction: column; color: var(--white); }
  .brand-name {
    font-weight: 700;
    font-size: 30px;
    letter-spacing: 1.5px;
    line-height: 1;
  }
  .brand-tag {
    font-weight: 700;
    font-size: 9.5px;
    letter-spacing: 12.6px;
    margin-top: 6px;
    line-height: 1;
  }

  .contact-list {
    position: absolute;
    left: 238px;
    top: 150px;
    list-style: none;
    color: var(--white);
    font-size: 16.5px;
    line-height: 21px;
  }
  .contact-item { display: flex; align-items: flex-start; gap: 8px; margin-bottom: 12px; }
  .contact-item:first-child { align-items: center; }
  .contact-icon { flex: none; width: 30px; height: 30px; margin-top: -2px; }
  .contact-item.email .contact-icon { margin-top: 4px; }
</style>
</head>
<body>

  <section class="card card-front" aria-label="Business card front">
    <svg class="card-shape" viewBox="0 0 640 366" preserveAspectRatio="none" aria-hidden="true">
      <polygon points="0,0 335,0 0,320" fill="var(--blue)"/>
    </svg>
    <div class="brand">
      <span class="brand-mark" aria-hidden="true"></span>
      <div class="brand-text">
        <span class="brand-name">KELMORA</span>
        <span class="brand-tag">CONSULTING</span>
      </div>
    </div>
  </section>

  <section class="card card-back" aria-label="Business card back">
    <svg class="card-shape" viewBox="0 0 640 366" preserveAspectRatio="none" aria-hidden="true">
      <polygon points="0,0 305,0 0,290" fill="var(--navy)"/>
    </svg>
    <ul class="contact-list">
      <li class="contact-item phone">
        <svg class="contact-icon" viewBox="0 0 30 30" aria-hidden="true">
          <circle cx="15" cy="15" r="15" fill="var(--navy)"/>
          <path d="M10.5 8.5l2.5-.5 1.5 3.5-1.7 1.2a8 8 0 0 0 4 4l1.2-1.7 3.5 1.5-.5 2.5c-.3 1-1.3 1.5-2.3 1.3A11 11 0 0 1 9.2 10.8c-.2-1 .3-2 1.3-2.3z" fill="var(--white)"/>
        </svg>
        <span>+1 000 000 0000</span>
      </li>
      <li class="contact-item address">
        <svg class="contact-icon" viewBox="0 0 30 30" aria-hidden="true">
          <circle cx="15" cy="15" r="15" fill="var(--navy)"/>
          <path d="M15 7a5.5 5.5 0 0 0-5.5 5.5C9.5 17 15 23 15 23s5.5-6 5.5-10.5A5.5 5.5 0 0 0 15 7z" fill="var(--white)"/>
          <circle cx="15" cy="12.5" r="2" fill="var(--navy)"/>
        </svg>
        <span>000 Lorem ipsum dolor sit amet,<br>consectetuer adipiscing elit, sed<br>United States, State, Zip code</span>
      </li>
      <li class="contact-item email">
        <svg class="contact-icon" viewBox="0 0 30 30" aria-hidden="true">
          <circle cx="15" cy="15" r="15" fill="var(--navy)"/>
          <rect x="8" y="10" width="14" height="10" rx="1.5" fill="none" stroke="var(--white)" stroke-width="1.6"/>
          <path d="M8.5 11l6.5 5 6.5-5" fill="none" stroke="var(--white)" stroke-width="1.6"/>
        </svg>
        <span>Email us @ Kelmoraconsulting.com<br>info@kelmoraconsulting.com</span>
      </li>
    </ul>
  </section>

</body>
</html>
```